Poster

I need a poster for my business, www.coastaltablejourneysbay.example which some information about the most important activities (Sangria Tasting, Iberian Ham, Charcuteries & Sherry Wine Tasting, Sailboat Experiences and Picnic Experiences). A3 Format. Social media included (@coastaltablejourneyctj), contact information included.

```html
<!DOCTYPE html>
<html lang="en">
<head>
<meta charset="UTF-8">
<title>Coastal Table Journeys – Poster</title>
<link rel="stylesheet" href="https://fonts.googleapis.com/css2?family=Bebas+Neue&family=Montserrat:wght@600;700&display=swap">
<style>
  :root {
    --orange: #f0a21c;
    --ink: #423f42;
    --panel: #f6eef4;
    --dusk-top: #efe6ee;
    --dusk-mid: #d9d3d6;
    --dusk-low: #b9b5a8;
    --band-dark: #3f3d40;
    --white: #ffffff;
  }
  * { box-sizing: border-box; margin: 0; padding: 0; }
  html, body { width: 880px; height: 1200px; overflow: hidden; }
  body { background: var(--orange); font-family: "Bebas Neue", "Arial Narrow", sans-serif; color: var(--ink); }

  .poster { position: relative; width: 880px; height: 1200px; background: var(--orange); }
  .panel {
    position: absolute; left: 20px; top: 20px; right: 20px; bottom: 20px;
    background: var(--panel); overflow: hidden;
  }
  .panel-scenery {
    position: absolute; left: 0; right: 0; top: 560px; bottom: 0;
    background: linear-gradient(180deg, var(--panel) 0%, var(--dusk-top) 25%, var(--dusk-mid) 55%, var(--dusk-low) 100%);
  }

  .brand { position: absolute; top: 60px; left: 0; right: 0; display: flex; flex-direction: column; align-items: center; }
  .brand-name { font-size: 66px; line-height: 0.92; text-align: center; color: var(--ink); letter-spacing: 0.5px; }
  .brand-tag {
    margin-top: 14px; width: 262px; height: 42px; background: var(--orange); color: var(--white);
    font-family: "Montserrat", sans-serif; font-weight: 600; font-size: 19px; letter-spacing: 1px;
    display: flex; align-items: center; justify-content: center;
  }

  .activity { position: absolute; width: 300px; text-align: center; }
  .activity-photo {
    display: block; margin: 0 auto; width: 216px; height: 216px; border-radius: 50%;
    border: 5px solid var(--orange);
  }
  .activity-title { margin-top: 12px; font-size: 50px; line-height: 0.98; color: var(--ink); }

  .photo-sangria   { background: radial-gradient(circle at 55% 55%, #7a1d2a 0 25%, #a08a70 45%, #8c7862 100%); }
  .photo-ham       { background: radial-gradient(circle at 50% 60%, #b63a4a 0 25%, #c59a6e 50%, #7d8a8c 100%); }
  .photo-board     { background: radial-gradient(circle at 50% 55%, #e6c978 0 20%, #8c6a4a 55%, #4a3a30 100%); }
  .photo-sailboat  { background: linear-gradient(180deg, #4c8fd6 0%, #9cc6ea 35%, #1f4f7a 50%, #2a3440 100%); }
  .photo-picnic    { background: linear-gradient(180deg, #4f7a3a 0%, #8aa06a 35%, #e3d2d8 60%, #cfb8a8 100%); }

  .a-sangria  { left: 5px;   top: 325px; }
  .a-ham      { left: 266px; top: 325px; }
  .a-board    { left: 526px; top: 325px; }
  .a-sailboat { left: 122px; top: 712px; }
  .a-picnic   { left: 437px; top: 712px; }

  .social { position: absolute; left: 0; right: 0; top: 1060px; text-align: center;
    font-family: "Montserrat", sans-serif; font-weight: 700; font-size: 17px; color: var(--ink); }

  .footer-wave { position: absolute; left: 0; bottom: 0; width: 840px; height: 120px; }
  .contact {
    position: absolute; left: 30px; right: 20px; bottom: 14px; display: flex; align-items: center; gap: 28px;
    font-family: "Montserrat", sans-serif; font-weight: 700; font-size: 19px; color: var(--white);
  }
  .contact-item { display: flex; align-items: center; gap: 10px; }
  .contact-item svg { width: 28px; height: 28px; flex: none; }
</style>
</head>
<body>
<div class="poster">
  <div class="panel">
    <div class="panel-scenery" role="img" aria-label="Evening view of a seaside town with lights along the coast"></div>

    <header class="brand">
      <h1 class="brand-name">Coastal Table<br>Journeys</h1>
      <div class="brand-tag">BAY</div>
    </header>

    <section class="activity a-sangria">
      <div class="activity-photo photo-sangria" role="img" aria-label="Glass of sangria with an orange slice"></div>
      <h2 class="activity-title">Sangria<br>Tasting</h2>
    </section>
    <section class="activity a-ham">
      <div class="activity-photo photo-ham" role="img" aria-label="Sliced cured ham on a wooden board with a glass of wine"></div>
      <h2 class="activity-title">Iberian<br>Ham</h2>
    </section>
    <section class="activity a-board">
      <div class="activity-photo photo-board" role="img" aria-label="Charcuterie board with cheeses, olives and grapes"></div>
      <h2 class="activity-title">Charcuteries<br>&amp; Sherry Wine<br>Tasting</h2>
    </section>
    <section class="activity a-sailboat">
      <div class="activity-photo photo-sailboat" role="img" aria-label="Sailboat deck heading out to open sea"></div>
      <h2 class="activity-title">Sailboat<br>Experiences</h2>
    </section>
    <section class="activity a-picnic">
      <div class="activity-photo photo-picnic" role="img" aria-label="Decorated outdoor picnic table in a garden"></div>
      <h2 class="activity-title">Picnic<br>Experiences</h2>
    </section>

    <p class="social">@coastaltablejourneyctj</p>

    <svg class="footer-wave" viewBox="0 0 840 120" preserveAspectRatio="none" aria-hidden="true">
      <path d="M0 20 C 220 75, 560 75, 840 28 L 840 120 L 0 120 Z" fill="var(--band-dark)"/>
      <path d="M0 38 C 240 88, 580 82, 840 46 L 840 120 L 0 120 Z" fill="var(--orange)"/>
    </svg>

    <footer class="contact">
      <span class="contact-item">
        <svg viewBox="0 0 24 24" aria-hidden="true"><path fill="#fff" d="M6.6 10.8a15.1 15.1 0 0 0 6.6 6.6l2.2-2.2a1 1 0 0 1 1-.25 11.4 11.4 0 0 0 3.6.57 1 1 0 0 1 1 1V20a1 1 0 0 1-1 1A17 17 0 0 1 3 4a1 1 0 0 1 1-1h3.5a1 1 0 0 1 1 1c0 1.25.2 2.45.57 3.57a1 1 0 0 1-.25 1z"/></svg>
        +34 611 22 33 44
      </span>
      <span class="contact-item">
        <svg viewBox="0 0 24 24" aria-hidden="true" fill="none" stroke="#fff" stroke-width="2.2"><circle cx="12" cy="12" r="9.5"/><ellipse cx="12" cy="12" rx="4" ry="9.5"/><path d="M2.5 12h19"/></svg>
        www.coastaltablejourneysbay.example
      </span>
    </footer>
  </div>
</div>
</body>
</html>
```